New Business Card

We need to refresh our business cards. We designed these ourselves and we have no graphic design experience. We would like to find a new business card design that is professional and unique. We are an auto finance company. Feel free to play with the logo, but we would like to keep the eye very present on the card. Our corporate colors are green, grey, and white.
Green - RGB - 168,215,27; HEX - #AADD22
Grey - RGB - 196,196,196; HEX - #C4C4C4
Need to upload the vector file to finalize the project. The last logo was for a jpeg that didn't stretch well.
Industry/Entity Type
Financial Service
Contact Information for Business Card
Honestly don't know...I need your help!

```html
<!DOCTYPE html>
<html lang="en">
<head>
<meta charset="utf-8">
<title>Northvale Capital – Business Card</title>
<link rel="stylesheet" href="https://fonts.googleapis.com/css2?family=Pathway+Gothic+One&display=swap">
<style>
  :root {
    --green: #aadd22;
    --green-text: #a8cf3c;
    --green-soft: #b9d865;
    --grey: #c4c4c4;
    --grey-shadow: #9c9c9c;
    --white: #ffffff;
    --font: "Pathway Gothic One", "Arial Narrow", sans-serif;
  }
  html, body {
    margin: 0;
    padding: 0;
    width: 1200px;
    height: 686px;
    overflow: hidden;
    background: var(--white);
  }
  .card {
    position: relative;
    width: 1200px;
    height: 686px;
    background: var(--white);
    font-family: var(--font);
    overflow: hidden;
  }
  .card-backdrop {
    position: absolute;
    inset: 0;
  }
  .identity {
    position: absolute;
    left: 0;
    width: 530px;
    top: 118px;
    text-align: center;
    color: var(--green-soft);
  }
  .identity-name {
    margin: 0;
    font-size: 56px;
    line-height: 1;
    font-weight: 400;
  }
  .identity-title {
    margin: 4px 0 0;
    font-size: 37px;
    line-height: 1;
  }
  .divider {
    position: absolute;
    left: 63px;
    top: 266px;
    width: 392px;
    height: 4px;
    background: var(--green-text);
  }
  .contact-list {
    position: absolute;
    left: 64px;
    top: 348px;
    margin: 0;
    padding: 0;
    list-style: none;
  }
  .contact-item {
    display: flex;
    align-items: center;
    height: 52px;
    margin-bottom: 15px;
    color: var(--green-text);
    font-size: 36px;
  }
  .contact-icon {
    width: 52px;
    height: 52px;
    margin-right: 10px;
    flex: none;
  }
  .wordmark {
    position: absolute;
    left: 792px;
    top: 278px;
    color: var(--green);
    font-weight: 400;
    line-height: 1;
  }
  .wordmark-name {
    display: block;
    font-size: 82px;
  }
  .wordmark-sub {
    display: block;
    margin-top: 6px;
    font-size: 34px;
    letter-spacing: 22px;
    text-transform: uppercase;
  }
</style>
</head>
<body>
<div class="card">
  <svg class="card-backdrop" width="1200" height="686" viewBox="0 0 1200 686" aria-hidden="true">
    <rect class="panel-grey" x="602" y="0" width="598" height="686" fill="var(--grey)"/>
    <rect class="accent-stripe" x="589" y="0" width="13" height="686" fill="var(--green)"/>
    <rect class="tab-shadow" x="468" y="225" width="760" height="239" rx="118" fill="var(--grey-shadow)"/>
    <rect class="tab" x="470" y="222" width="760" height="239" rx="118" fill="var(--white)"/>
    <circle class="brand-dot" cx="640" cy="338" r="72" fill="var(--grey)"/>
  </svg>

  <header class="identity">
    <h1 class="identity-name">Daniel Hart</h1>
    <p class="identity-title">President</p>
  </header>

  <div class="divider"></div>

  <ul class="contact-list">
    <li class="contact-item">
      <svg class="contact-icon" viewBox="0 0 52 52" aria-hidden="true">
        <rect x="16" y="5" width="20" height="38" rx="3" fill="none" stroke="var(--green-text)" stroke-width="3"/>
        <line x1="17" y1="34" x2="35" y2="34" stroke="var(--green-text)" stroke-width="2"/>
        <circle cx="26" cy="39" r="1.8" fill="var(--green-text)"/>
        <path d="M10 9 q-3 4 0 8 M6 7 q-5 6 0 12 M42 9 q3 4 0 8 M46 7 q5 6 0 12" fill="none" stroke="var(--green-text)" stroke-width="1.6"/>
      </svg>
      <span class="contact-text">555-014-2278</span>
    </li>
    <li class="contact-item">
      <svg class="contact-icon" viewBox="0 0 52 52" aria-hidden="true">
        <rect x="2" y="14" width="46" height="24" fill="var(--green-text)"/>
        <path d="M2 14 L25 30 L48 14 M2 38 L19 26 M48 38 L31 26" fill="none" stroke="var(--white)" stroke-width="2"/>
      </svg>
      <span class="contact-text">info@northvalecap.com</span>
    </li>
    <li class="contact-item">
      <svg class="contact-icon" viewBox="0 0 52 52" aria-hidden="true">
        <g fill="none" stroke="var(--green-text)" stroke-width="2.2">
          <circle cx="26" cy="26" r="21"/>
          <ellipse cx="26" cy="26" rx="9" ry="21"/>
          <line x1="26" y1="5" x2="26" y2="47"/>
          <line x1="5" y1="26" x2="47" y2="26"/>
          <path d="M9 14 h34 M9 38 h34"/>
        </g>
      </svg>
      <span class="contact-text">www.northvalecap.com</span>
    </li>
  </ul>

  <div class="wordmark">
    <span class="wordmark-name">Northvale</span>
    <span class="wordmark-sub">Capital</span>
  </div>
</div>
</body>
</html>
```